Business Card Design for Pastor/Church Leadership - simple, elegant, "different"

Design a name card based on logo and color from our branding guide - see file "MBF Logo and Color".
The teal frame around the logo is not part of the logo and is a not necessary design element for the name card (as the attached PDF file may suggest).
The font suggested by branding is "Frutiger 55 Roman".
The file "not good.pdf", a sample of a name card that is NOT good.
- fonts too small to read
- the tagline on the logo "Still waters, open door" not easy to read with logo used in this design
- "MAPLE GROVE FELLOWSHIP" unnecessarily duplicated - possibly because logo too small
- not sure about the green frame, probably better to drop

Target Market(s)

broad, all people the pastor of an international church in Tokyo meets

Industry/Entity Type

Business

Contact Information for Business Card

Mattias R. Pellworth
Pastor
3-9-4 Kawaranodai, Shibuya-ku
Tokyo 150-0001 (Church)
2-21 Ochibamachi, Shibuya-ku
Tokyo 150-0035 (Home)
Tel: 03-5817-2963
E-mail: pastor@maplegrovefell.org
URL: http://www.maplegrovefell.org

Font styles to use
Sans Serif
Other font styles liked:
• Frutiger 55 Roman (want, not must)

Requirements
Must have
• must include logo
• must make use of the "bright turquoise color"
• Cyan = 59, Magenta = 0, Yellow=24, Black=0
• Red=3.1%, Green=91%, Blue=87.1%
• Key Info (name) must be easy to read (see notes on bad sample namecard attached)

```html
<!DOCTYPE html>
<html lang="en">
<head>
<meta charset="utf-8">
<title>Maple Grove Fellowship – Pastor Business Card</title>
<link href="https://fonts.googleapis.com/css2?family=Open+Sans:wght@400&family=Roboto+Slab:wght@300;400&display=swap" rel="stylesheet">
<style>
  :root {
    --teal: #5bc3c4;
    --teal-soft: rgba(91, 195, 196, 0.55);
    --teal-fade: rgba(91, 195, 196, 0);
    --ink: #1f1f1f;
    --paper: #ffffff;
    --backdrop: #e9ecec;
    --slab: "Roboto Slab", Georgia, serif;
    --sans: "Open Sans", Arial, sans-serif;
  }
  * { margin: 0; padding: 0; box-sizing: border-box; }
  html, body { width: 1200px; height: 788px; overflow: hidden; }
  body {
    background: var(--backdrop);
    display: flex; align-items: center; justify-content: center;
  }
  .card {
    position: relative;
    width: 1080px; height: 654px;
    background: var(--paper);
    overflow: hidden;
    box-shadow: 0 6px 24px rgba(0,0,0,.12);
  }

  .card__accent {
    position: absolute; top: 0; right: 0;
    width: 620px; height: 330px;
    background: radial-gradient(ellipse 100% 100% at 100% 0%,
      var(--teal-soft) 0%, var(--teal-fade) 100%);
  }

  .contact {
    position: absolute; left: 62px;
    font-family: var(--slab); font-weight: 300;
    color: var(--teal); font-size: 21px; line-height: 28px;
    list-style: none;
  }
  .contact li { display: flex; align-items: flex-start; gap: 16px; }
  .contact .icon {
    flex: none; width: 26px; height: 26px; margin-top: 1px;
    stroke: var(--ink); fill: none; stroke-width: 1.6;
  }
  .contact--address { top: 200px; }
  .contact--address li { margin-bottom: 4px; }
  .contact--reach { top: 388px; }
  .contact--reach li { margin-bottom: 6px; }

  .person { position: absolute; left: 62px; bottom: 64px; }
  .person__name {
    font-family: var(--slab); font-weight: 400;
    font-size: 36px; color: var(--ink); letter-spacing: .2px;
  }
  .person__role {
    font-family: var(--slab); font-weight: 300;
    font-size: 21px; color: var(--teal); letter-spacing: 1px;
  }

  .brand {
    position: absolute; left: 590px; top: 380px; width: 400px;
    text-align: center; font-family: var(--sans); font-weight: 400;
    color: var(--teal);
  }
  .brand__mark {
    width: 22px; height: 22px; border-radius: 50%;
    background: var(--teal); margin: 0 auto 16px;
  }
  .brand__name { font-size: 21px; letter-spacing: 3.5px; }
  .brand__rule { height: 2px; background: var(--teal); margin: 8px 10px 10px; }
  .brand__tagline { font-size: 19px; letter-spacing: 2px; }
</style>
</head>
<body>
  <main class="card">
    <div class="card__accent" role="img" aria-label="Decorative sweeping turquoise bands along the top and right edges"></div>

    <ul class="contact contact--address">
      <li>
        <svg class="icon" viewBox="0 0 26 26"><circle cx="13" cy="13" r="11"/><path d="M13 6 L13 20 M9 10 L17 10"/></svg>
        <span>3-9-4 Kawaranodai, Shibuya-ku<br>Tokyo 150-0001 (Church)</span>
      </li>
      <li>
        <svg class="icon" viewBox="0 0 26 26"><circle cx="13" cy="13" r="11"/><path d="M7 14 L13 8 L19 14 M9 13 V19 H17 V13"/></svg>
        <span>2-21 Ochibamachi, Shibuya-ku<br>Tokyo 150-0035 (Home)</span>
      </li>
    </ul>

    <ul class="contact contact--reach">
      <li>
        <svg class="icon" viewBox="0 0 26 26"><circle cx="13" cy="13" r="11"/><path d="M9 7 L11 7 L12 10 L10.5 11.5 Q12 14.5 14.5 15.5 L16 14 L19 15 L19 17 Q15 19 11 15 Q7 11 9 7 Z"/></svg>
        <span>03-5817-2963</span>
      </li>
      <li>
        <svg class="icon" viewBox="0 0 26 26"><circle cx="13" cy="13" r="11"/><path d="M2 13 H24 M13 2 Q7 13 13 24 M13 2 Q19 13 13 24"/></svg>
        <span>pastor@maplegrovefell.org</span>
      </li>
      <li>
        <svg class="icon" viewBox="0 0 26 26"><rect x="2" y="6" width="22" height="14"/><path d="M2 6 L13 15 L24 6"/></svg>
        <span>www.maplegrovefell.org</span>
      </li>
    </ul>

    <div class="person">
      <p class="person__name">Mattias R. Pellworth</p>
      <p class="person__role">PASTOR</p>
    </div>

    <div class="brand">
      <div class="brand__mark"></div>
      <p class="brand__name">MAPLE GROVE FELLOWSHIP</p>
      <div class="brand__rule"></div>
      <p class="brand__tagline">Still waters, open door</p>
    </div>
  </main>
</body>
</html>
```